Commercial Construction Company

We need a business card design based on our current logo. We are a commercial general contractor based in Southern California that specializes in bank remodels. We would like to see designs that incorporate dark blue. The final design should portray an image of professionalism and quality.

If possible, I would like to add metallic foil to the design. Thank you

```html
<!DOCTYPE html>
<html lang="en">
<head>
<meta charset="utf-8">
<title>Harlow Commercial Building Group – Business Card</title>
<link rel="stylesheet" href="https://fonts.googleapis.com/css2?family=Montserrat:wght@800&family=Arimo:wght@400&display=swap">
<style>
  :root {
    --navy: #0f4a82;
    --ink: #111111;
    --grey-band: #c7c7c7;
    --grey-soft: #f1f1f1;
    --paper: #ffffff;
    --text: #2a2a2a;
    --rule: #bdbdbd;
    --backdrop: #2c2c2c;
  }
  * { box-sizing: border-box; margin: 0; padding: 0; }
  html, body { width: 1200px; height: 866px; overflow: hidden; background: var(--backdrop); }
  .canvas { position: relative; width: 1200px; height: 866px; }

  .card {
    position: absolute; top: 273px; width: 560px; height: 320px;
    overflow: hidden; box-shadow: 0 10px 26px rgba(0,0,0,.45);
  }
  .card--front { left: 25px; background: var(--paper); }
  .card--back { left: 615px; background: var(--navy); }

  .card__wash {
    position: absolute; left: 0; top: 0; right: 0; height: 110px;
    background: linear-gradient(180deg, var(--grey-soft) 0%, rgba(255,255,255,0) 100%);
  }

  .contact { position: absolute; left: 36px; top: 66px; font-family: "Arimo", sans-serif; color: var(--text); }
  .contact__name { font-family: "Montserrat", sans-serif; font-weight: 800; font-size: 19px; color: var(--navy); letter-spacing: .5px; text-transform: uppercase; }
  .contact__title { font-size: 14px; color: #444; margin: 2px 0 12px; }
  .contact__line { display: flex; align-items: center; gap: 8px; font-size: 13.5px; line-height: 20px; }
  .contact__line svg { width: 13px; height: 13px; fill: var(--navy); flex: none; }

  .brand { position: absolute; display: flex; align-items: center; gap: 14px; font-family: "Montserrat", sans-serif; font-weight: 800; }
  .brand__dot { border-radius: 50%; flex: none; }
  .brand__name { display: block; text-transform: uppercase; letter-spacing: 1px; }

  .card--front .brand { left: 290px; top: 92px; color: var(--ink); }
  .card--front .brand__dot { width: 52px; height: 52px; background: var(--navy); }
  .card--front .brand__name { font-size: 20px; line-height: 24px; width: 190px; }

  .rule { position: absolute; left: 200px; right: 30px; top: 208px; height: 1px; background: var(--rule); }

  .address { position: absolute; right: 30px; top: 222px; text-align: right; font-family: "Arimo", sans-serif; font-size: 14px; line-height: 19px; color: #333; }

  .band { position: absolute; bottom: 0; }
  .band--grey { left: 0; width: 230px; height: 6px; background: var(--grey-band); }
  .band--navy { left: 230px; right: 0; height: 14px; background: var(--navy); }

  .card--back .brand { left: 50%; top: 50%; transform: translate(-50%, -50%); color: var(--paper); }
  .card--back .brand__dot { width: 60px; height: 60px; background: var(--paper); }
  .card--back .brand__name { font-size: 24px; line-height: 29px; width: 230px; }
</style>
</head>
<body>
<main class="canvas">

  <section class="card card--front" aria-label="Business card front">
    <div class="card__wash" role="img" aria-label="Soft grey curved decoration across the top of the card"></div>

    <div class="contact">
      <p class="contact__name">Daniel Marsh</p>
      <p class="contact__title">Managing Director</p>
      <p class="contact__line"><svg viewBox="0 0 16 16" aria-hidden="true"><path d="M3 1h3l1 4-2 1a9 9 0 0 0 5 5l1-2 4 1v3a2 2 0 0 1-2 2A13 13 0 0 1 1 3a2 2 0 0 1 2-2z"/></svg>044-555 018 204</p>
      <p class="contact__line"><svg viewBox="0 0 16 16" aria-hidden="true"><path d="M1 3h14v10H1z M1 3l7 6 7-6" stroke="#fff" stroke-width="1.2"/></svg>hello@harlowbuild.com</p>
      <p class="contact__line"><svg viewBox="0 0 16 16" aria-hidden="true"><circle cx="8" cy="8" r="7"/></svg>www.harlowbuild.com</p>
    </div>

    <div class="brand">
      <span class="brand__dot"></span>
      <span class="brand__name">Harlow Commercial Building Group</span>
    </div>

    <div class="rule"></div>

    <p class="address">12345, Address Goes Here<br>Country Name, 123456</p>

    <div class="band band--grey"></div>
    <div class="band band--navy"></div>
  </section>

  <section class="card card--back" aria-label="Business card back">
    <div class="brand">
      <span class="brand__dot"></span>
      <span class="brand__name">Harlow Commercial Building Group</span>
    </div>
  </section>

</main>
</body>
</html>
```